The Pebble Lantern Business Card

I need a business card designed for The Pebble Lantern. The company provides on site support and education to end consumers in the ins and outs of all our digital devices. We advise on product purchase, installation, maintenance and troubleshooting. Anything from cordless phones to home networks.
My initial concept is double sided with the white logo on green on one side and contact details and a small logo on the flip side (logo package attached)
Contact Details:
Marty Fenwick
Managing Director
PO Box 3
Wattlebury, NSW 2047
Phone: 0438 605 193
email: marty@pebblelantern.com.au
web: www.pebblelantern.com.au
Target Market(s)
Busy professionals and retired folks.
Industry/Entity Type
Education
Look and feel

```html
<!DOCTYPE html>
<html lang="en">
<head>
<meta charset="utf-8">
<title>The Pebble Lantern – Business Card</title>
<link rel="stylesheet" href="https://fonts.googleapis.com/css2?family=Montserrat:wght@400;600&family=Questrial&display=swap">
<style>
  :root {
    --leaf-green: #7cb33a;
    --leaf-green-dark: #6ea42f;
    --ink-navy: #1b2c45;
    --paper: #ffffff;
    --backdrop: #eef0ea;
  }
  * { box-sizing: border-box; margin: 0; padding: 0; }
  html, body {
    width: 1200px; height: 784px; overflow: hidden;
    background: var(--backdrop);
  }
  .canvas {
    position: relative; width: 1200px; height: 784px;
  }
  .card {
    position: absolute; top: 227px;
    width: 540px; height: 330px;
    overflow: hidden;
    box-shadow: 0 6px 18px rgba(0,0,0,0.15);
  }
  /* Front side */
  .card--front {
    left: 40px;
    background: var(--leaf-green);
  }
  .front-brand {
    position: absolute; left: 0; top: 0; width: 100%; height: 100%;
    display: flex; align-items: center; justify-content: center; gap: 20px;
  }
  .brand-dot {
    width: 56px; height: 56px; border-radius: 50%;
    background: var(--paper);
  }
  .front-brand .brand-name {
    font-family: "Questrial", sans-serif;
    font-size: 42px; color: var(--paper);
    letter-spacing: 0.5px;
  }
  /* Back side */
  .card--back {
    left: 620px;
    background: var(--paper);
  }
  .card-shapes { position: absolute; inset: 0; }
  .back-brand {
    position: absolute; left: 42px; top: 70px;
    display: flex; align-items: center; gap: 14px;
  }
  .back-brand .brand-dot {
    width: 34px; height: 34px; background: var(--leaf-green);
  }
  .back-brand .brand-name {
    font-family: "Questrial", sans-serif;
    font-size: 28px; color: var(--ink-navy);
  }
  .holder {
    position: absolute; left: 130px; top: 232px; text-align: right;
    width: 170px;
  }
  .holder-name {
    font-family: "Montserrat", sans-serif; font-weight: 600;
    font-size: 16px; color: var(--ink-navy);
  }
  .holder-role {
    font-family: "Montserrat", sans-serif; font-weight: 400;
    font-size: 11.5px; color: var(--paper); margin-top: 4px;
  }
  .contact-list {
    position: absolute; left: 316px; top: 196px;
    list-style: none;
    border-left: 1.5px solid var(--paper);
    padding-left: 8px;
  }
  .contact-list li {
    display: flex; align-items: center; gap: 6px;
    font-family: "Montserrat", sans-serif; font-size: 11px;
    color: var(--paper); height: 21px; white-space: nowrap;
  }
  .contact-list svg { width: 14px; height: 14px; flex: none; }
</style>
</head>
<body>
<main class="canvas">

  <section class="card card--front" aria-label="Business card front">
    <div class="front-brand">
      <span class="brand-dot"></span>
      <span class="brand-name">The Pebble Lantern</span>
    </div>
  </section>

  <section class="card card--back" aria-label="Business card back">
    <svg class="card-shapes" viewBox="0 0 540 330" width="540" height="330" aria-hidden="true">
      <path d="M0,330 L0,290 C140,200 330,175 540,45 L540,330 Z" fill="var(--leaf-green)"/>
      <path d="M290,160 C410,125 490,75 540,8 L540,36 C470,100 390,140 290,160 Z" fill="var(--ink-navy)"/>
    </svg>

    <div class="back-brand">
      <span class="brand-dot"></span>
      <span class="brand-name">The Pebble Lantern</span>
    </div>

    <div class="holder">
      <p class="holder-name">Marty Fenwick</p>
      <p class="holder-role">Managing Director</p>
    </div>

    <ul class="contact-list">
      <li>
        <svg viewBox="0 0 16 16" aria-hidden="true"><path d="M4 1.5l2.2 3-1.3 1.6c.8 1.8 2.2 3.2 4 4l1.6-1.3 3 2.2-1.3 2.8C6.5 13.6 2.4 9.5 1.5 3.8z" fill="var(--ink-navy)"/></svg>
        0438 605 193
      </li>
      <li>
        <svg viewBox="0 0 16 16" aria-hidden="true"><rect x="1.5" y="3.5" width="13" height="9" rx="1" fill="none" stroke="var(--ink-navy)" stroke-width="1.5"/><path d="M1.5 4l6.5 5 6.5-5" fill="none" stroke="var(--ink-navy)" stroke-width="1.5"/></svg>
        marty@pebblelantern.com.au
      </li>
      <li>
        <svg viewBox="0 0 16 16" aria-hidden="true"><circle cx="8" cy="8" r="6.3" fill="none" stroke="var(--ink-navy)" stroke-width="1.4"/><ellipse cx="8" cy="8" rx="2.8" ry="6.3" fill="none" stroke="var(--ink-navy)" stroke-width="1.2"/><path d="M1.7 8h12.6" stroke="var(--ink-navy)" stroke-width="1.2"/></svg>
        www.pebblelantern.com.au
      </li>
      <li>
        <svg viewBox="0 0 16 16" aria-hidden="true"><path d="M8 1.5L1 8h2v6.5h4v-4h2v4h4V8h2z" fill="var(--ink-navy)"/></svg>
        PO Box 3, Wattlebury, NSW 2047
      </li>
    </ul>
  </section>

</main>
</body>
</html>
```